VornaDerm/The experts in permanent hairremoval

Our Brand is VornaDerm and we are specialized on permantent hair removal for the body for men and woman. VornaDerm is working as a Franchise chain.
The brand should be positioned as lifestyle brand but with a medical background. People should trust in us. We take care about their body. This need to be communicated 100%.
Our system is inexpensive but we don't want to show that we are cheap. So we want to communicate that permanent hair removal is a real lifestyle product but affordable.
We already created a logo that you can see the style and colour we prefer.

Target Market(s)

Europe beginning (especially german spoken markets), Middle East, Africa

Industry/Entity Type

Hair Removal

Number of Pages Required

5+ page

Font styles to use
Serif
Other font styles liked:
• Trajan Pro

Requirements
Nice to have
• We are very open for new ideas

```html
<!DOCTYPE html>
<html lang="en">
<head>
<meta charset="utf-8">
<title>VornaDerm – The experts in permanent hair removal</title>
<link href="https://fonts.googleapis.com/css2?family=Open+Sans:wght@300;400;600;700&display=swap" rel="stylesheet">
<style>
:root{
  --blue:#72b3e3;
  --blue-text:#5fa8dc;
  --navy:#2c5d8f;
  --orange:#f0a80e;
  --grey-text:#6d6d6d;
  --grey-dark:#4a4a4a;
  --hero-bg:#d9dee4;
  --footer:#464646;
  --footer-bottom:#3b3b3b;
  --rule:#d6d6d6;
  --white:#ffffff;
}
*{margin:0;padding:0;box-sizing:border-box}
html,body{width:715px;height:1200px;overflow:hidden;background:var(--white)}
body{position:relative;font-family:"Open Sans",Arial,sans-serif;color:var(--grey-text)}
.abs{position:absolute}
ul{list-style:none}

/* header */
.brand{left:59px;top:14px;display:flex;align-items:center;gap:8px}
.brand-mark{width:26px;height:26px;border-radius:50%;background:var(--blue)}
.brand-name{font-size:25px;font-weight:400;color:#7c7f83;letter-spacing:-.3px}
.call{left:381px;top:19px;display:flex;align-items:center;gap:7px;font-size:8px;color:var(--grey-dark)}
.call-icon{width:27px;height:27px;border-radius:50%;background:var(--blue);display:flex;align-items:center;justify-content:center}
.call b{font-weight:400;color:var(--blue-text)}
.btn{display:flex;align-items:center;justify-content:center;color:var(--white);font-weight:700;text-transform:uppercase;border-radius:2px}
.btn-book{left:523px;top:21px;width:134px;height:24px;background:var(--blue);font-size:7px}

/* nav */
.main-nav{left:0;top:63px;width:715px;height:24px;background:var(--blue);display:flex;align-items:center;padding-left:72px;gap:20.5px}
.main-nav a{color:var(--white);font-size:7.2px;text-decoration:none;text-transform:uppercase}

/* hero */
.hero{left:0;top:87px;width:715px;height:313px;background:linear-gradient(90deg,#eef0f3 0%,#dde2e8 60%,#d4d9df 100%)}
.hero-photo{position:absolute;left:0;top:0;width:452px;height:313px;background:linear-gradient(100deg,#f3f4f6 0%,#e6e3e1 45%,#dcdfe4 100%)}
.hero-title{position:absolute;left:391px;top:70px;font-size:40px;font-weight:700;color:#84878b;letter-spacing:-.5px}
.hero-lead{position:absolute;left:397px;top:122px;width:300px;font-size:14.6px;font-weight:300;line-height:20.5px;color:#5e6064}
.btn-join{position:absolute;left:399px;top:171px;width:101px;height:29px;background:var(--blue);font-size:8px}
.hero-dots{position:absolute;left:345px;top:294px;display:flex;gap:4px}
.hero-dots span{width:3.5px;height:3.5px;border-radius:50%;background:#b8bec6}
.hero-dots span:first-child{background:var(--blue)}

/* features */
.feature{top:425px;width:190px;display:flex;gap:9px}
.feature-icon{flex:none;width:29px;height:29px;border-radius:50%;background:var(--blue);display:flex;align-items:center;justify-content:center}
.feature h3{font-size:7.4px;font-weight:700;color:var(--blue-text);text-transform:uppercase;margin:4px 0 4px}
.feature p{font-size:6.4px;line-height:13.5px}

/* welcome */
.section-title{font-size:11.5px;font-weight:700;text-transform:uppercase}
.title-light{color:var(--blue-text)}
.title-dark{color:var(--navy)}
.welcome-photo{left:59px;top:534px;width:153px;height:96px;background:linear-gradient(135deg,#8a5f45 0%,#d9b9a3 50%,#eef0f2 100%)}
.welcome-text{font-size:6.5px;line-height:14.8px}
.list-what li{display:flex;align-items:center;gap:8px;font-size:6.5px;font-weight:600;color:#777;height:19px}

/* callout */
.callout{left:59px;top:706px;width:598px;height:54px;border:1px solid #cfcfcf}
.callout p{position:absolute;left:15px;top:10px;width:450px;font-size:7px;line-height:15px}
.btn-contact{position:absolute;left:473px;top:14px;width:110px;height:26px;background:var(--orange);font-size:7.5px}

/* stories & news */
.slider-arrows{display:flex;gap:3px}
.slider-arrows span{width:10px;height:10px;border-radius:50%;background:#dcdcdc;display:flex;align-items:center;justify-content:center}
.story{top:810px;width:183px}
.story-photo{height:102px}
.story h4,.news h4{font-size:7px;font-weight:700;color:#3a3a3a;text-transform:uppercase}
.story h4{margin:12px 0 6px}
.story p,.news p{font-size:6.4px;line-height:14.8px}
.news{left:479px;width:169px;padding-bottom:6px;border-bottom:1px solid var(--rule)}
.news h4{margin-bottom:4px}

/* footer */
.site-footer{left:0;top:1017px;width:715px;height:156px;background:var(--footer);color:var(--white)}
.footer-col{position:absolute;top:25px}
.footer-col h5{font-size:8px;font-weight:700;text-transform:uppercase;margin-bottom:6px}
.footer-col li{font-size:6.4px;line-height:14.4px}
.footer-brand{display:flex;align-items:center;gap:6px;margin-bottom:14px}
.footer-brand .brand-mark{width:20px;height:20px}
.footer-brand span{font-size:18px;color:#b7babe}
.social{display:flex;gap:6px;margin-top:10px}
.social span{width:16px;height:16px;border-radius:50%;background:var(--white)}
.footer-bottom{left:0;top:1173px;width:715px;height:27px;background:var(--footer-bottom);color:#e6e6e6;font-size:6.4px;display:flex;align-items:center;justify-content:center}
</style>
</head>
<body>

<header>
  <div class="abs brand"><span class="brand-mark"></span><span class="brand-name">VornaDerm</span></div>
  <div class="abs call">
    <span class="call-icon"><svg width="12" height="12" viewBox="0 0 24 24"><path fill="#fff" d="M6.6 10.8c1.4 2.8 3.8 5.1 6.6 6.6l2.2-2.2c.3-.3.7-.4 1-.2 1.1.4 2.3.6 3.6.6.6 0 1 .4 1 1V20c0 .6-.4 1-1 1C10.6 21 3 13.4 3 4c0-.6.4-1 1-1h3.5c.6 0 1 .4 1 1 0 1.3.2 2.5.6 3.6.1.3 0 .7-.2 1l-2.3 2.2z"/></svg></span>
    <span>Call Us : <b>( 4180 ) 735 219</b></span>
  </div>
  <a class="abs btn btn-book">Book your appointment</a>
</header>

<nav class="abs main-nav">
  <a>Why permanent epilation</a><a>Studios / Prices</a><a>Book your appointment</a><a>About VornaDerm</a><a>Jobs &amp; Careers</a><a>Franchise</a><a>Online shop</a>
</nav>

<section class="abs hero">
  <div class="hero-photo" role="img" aria-label="Woman in white sitting on a bed holding a white tulip"></div>
  <h1 class="hero-title">VornaDerm</h1>
  <p class="hero-lead">We are experts in permanent hair removal for the body for men and woman.</p>
  <a class="btn btn-join">Join with us</a>
  <div class="hero-dots"><span></span><span></span><span></span><span></span></div>
</section>

<section>
  <div class="abs feature" style="left:64px">
    <span class="feature-icon"><svg width="13" height="13" viewBox="0 0 24 24" fill="none" stroke="#fff" stroke-width="2.4"><rect x="3" y="4" width="16" height="16" rx="2"/><path d="M7 12l4 4 9-11"/></svg></span>
    <div><h3>The method</h3><p>Lorem Ipsum is simply dummy text of the printing and typesetting industry.</p></div>
  </div>
  <div class="abs feature" style="left:274px">
    <span class="feature-icon"><svg width="13" height="13" viewBox="0 0 24 24"><path fill="#fff" d="M2 10h4v11H2zM8 21h9.5c.9 0 1.6-.6 1.8-1.4l1.6-7c.2-1.2-.7-2.6-2-2.6H14l.8-4.2C15 4.4 14 3 12.7 3L8 10z"/></svg></span>
    <div><h3>Good to know</h3><p>Lorem Ipsum is simply dummy text of the printing and typesetting industry.</p></div>
  </div>
  <div class="abs feature" style="left:484px">
    <span class="feature-icon"><svg width="12" height="12" viewBox="0 0 24 24"><circle cx="12" cy="7" r="5" fill="#fff"/><path fill="#fff" d="M3 22c0-5 4-8 9-8s9 3 9 8z"/></svg></span>
    <div><h3>Zones</h3><p>Lorem Ipsum is simply dummy text of the printing and typesetting industry.</p></div>
  </div>
</section>

<section>
  <h2 class="abs section-title title-light" style="left:59px;top:503px">Welcome to VornaDerm</h2>
  <div class="abs welcome-photo" role="img" aria-label="Woman receiving a facial skin treatment"></div>
  <p class="abs welcome-text" style="left:232px;top:529px;width:190px">Lorem Ipsum is simply dummy text of the printing and type-setting industry. Lorem Ipsum has been the industry's stand-ard dummy text ever since the 1500s, when an unknown printer took a galley of type and scrambled it to make a type specimen book. It has survived not only five centuries, but also the leap into electronic typesetting, remaining essen-tially unchanged. It was popularised in the 1960s</p>
  <p class="abs welcome-text" style="left:61px;top:642px;width:372px">Lorem Ipsum is simply dummy text of the printing and typesetting industry. Lorem Ipsum has been the industry's standard dummy text ever since the 1500s, when an unknown printer took a galley of type and scrambled it to make a type specimen book. It has survived not only five centuries...</p>

  <h2 class="abs section-title title-light" style="left:463px;top:503px">What we do?</h2>
  <ul class="abs list-what" style="left:463px;top:526px">
    <li><svg width="7" height="6" viewBox="0 0 10 8"><path d="M1 4l3 3 5-6" fill="none" stroke="#f0a80e" stroke-width="2"/></svg>Lorem Ipsum is simply dummy text of printing</li>
    <li><svg width="7" height="6" viewBox="0 0 10 8"><path d="M1 4l3 3 5-6" fill="none" stroke="#f0a80e" stroke-width="2"/></svg>Lorem Ipsum is simply</li>
    <li><svg width="7" height="6" viewBox="0 0 10 8"><path d="M1 4l3 3 5-6" fill="none" stroke="#f0a80e" stroke-width="2"/></svg>Lorem Ipsum is simply dummy</li>
    <li><svg width="7" height="6" viewBox="0 0 10 8"><path d="M1 4l3 3 5-6" fill="none" stroke="#f0a80e" stroke-width="2"/></svg>Lorem Ipsum is simply dummy text</li>
    <li><svg width="7" height="6" viewBox="0 0 10 8"><path d="M1 4l3 3 5-6" fill="none" stroke="#f0a80e" stroke-width="2"/></svg>Lorem Ipsum is simply dummy text of the printing</li>
    <li><svg width="7" height="6" viewBox="0 0 10 8"><path d="M1 4l3 3 5-6" fill="none" stroke="#f0a80e" stroke-width="2"/></svg>Lorem Ipsum is simply</li>
    <li><svg width="7" height="6" viewBox="0 0 10 8"><path d="M1 4l3 3 5-6" fill="none" stroke="#f0a80e" stroke-width="2"/></svg>Lorem Ipsum is simply dummy text</li>
    <li><svg width="7" height="6" viewBox="0 0 10 8"><path d="M1 4l3 3 5-6" fill="none" stroke="#f0a80e" stroke-width="2"/></svg>Lorem Ipsum is simply dummy text of the printing</li>
  </ul>
</section>

<aside class="abs callout">
  <p>Lorem Ipsum is simply dummy text of the printing and typesetting industry. Lorem Ipsum has been the industry's standard dummy text ever since the 1500s, when an unknown printer took a galley of type and scrambled it to make a type specimen...</p>
  <a class="btn btn-contact">Contact now</a>
</aside>

<section>
  <h2 class="abs section-title title-dark" style="left:59px;top:781px">Successfull story</h2>
  <div class="abs slider-arrows" style="left:427px;top:784px"><span></span><span></span></div>
  <article class="abs story" style="left:59px">
    <div class="story-photo" role="img" aria-label="Client receiving laser underarm hair removal" style="background:linear-gradient(120deg,#c9c9c9,#e4d2c4 50%,#a8a8a8)"></div>
    <h4>Lorem ipsum is simply dummy</h4>
    <p>Lorem Ipsum is simply dummy text of the printing and typesetting industry. Lorem Ipsum has been the industry's standard dummy text ever since the 1500s</p>
  </article>
  <article class="abs story" style="left:268px">
    <div class="story-photo" role="img" aria-label="Smiling man touching his freshly treated cheek" style="background:linear-gradient(120deg,#d8dadd,#c79e83 50%,#e9e4d6)"></div>
    <h4>Lorem ipsum is simply dummy</h4>
    <p>Lorem Ipsum is simply dummy text of the printing and typesetting industry. Lorem Ipsum has been the industry's standard dummy text ever since the 1500s</p>
  </article>

  <h2 class="abs section-title title-dark" style="left:477px;top:781px">Latest news</h2>
  <div class="abs slider-arrows" style="left:632px;top:784px"><span></span><span></span></div>
  <article class="abs news" style="top:810px"><h4>Lorem ipsum is simply dummy</h4><p>Lorem Ipsum is simply dummy text of the printing and typesetting industry</p></article>
  <article class="abs news" style="top:870px"><h4>Lorem ipsum is simply dummy</h4><p>Lorem Ipsum is simply dummy text of the printing and typesetting industry</p></article>
  <article class="abs news" style="top:930px"><h4>Lorem ipsum is simply dummy</h4><p>Lorem Ipsum is simply dummy text of the printing and typesetting industry</p></article>
</section>

<footer class="abs site-footer">
  <div class="footer-col" style="left:59px"><h5>Welcome</h5>
    <ul><li>Why Permanent Epilation</li><li>Studios / Prices</li><li>Book your appointment</li><li>About VornaDerm</li><li>Jobs &amp; Careers</li><li>Franchise</li><li>Online Shop</li></ul></div>
  <div class="footer-col" style="left:207px"><h5>Contact info</h5>
    <ul><li>120 Street name, City name,</li><li>Country name : 6523652</li><li style="margin-top:3px">Phone : ( 4180 ) 735 219</li><li>Email : info@vornaderm.com</li></ul></div>
  <div class="footer-col" style="left:367px"><h5>Information</h5>
    <ul><li>Terms &amp; conditions</li><li>Privacy Policy</li><li>Disclaimer</li><li>Sitemap</li></ul></div>
  <div class="footer-col" style="left:515px;top:20px">
    <div class="footer-brand"><span class="brand-mark"></span><span>VornaDerm</span></div>
    <h5>Follow us</h5>
    <ul><li>Connect with our social media network</li></ul>
    <div class="social"><span></span><span></span><span></span><span></span><span></span></div>
  </div>
</footer>
<div class="abs footer-bottom">© 2015. VornaDerm. All rights reserved.</div>

</body>
</html>
```